logo and label design for a vegan skincare Called Leafmerelle

We need a logo and label design for a skincare brand called leafmerelle based in Australia. The products are 100% natural, Australian made, small batch, vegan, cruelty-free, ethical and sustainable beauty products. The secret of our skin care products are their naturally active ingredients.
They are potent, yet incredibly gentle on sensitive skin. We believe in investing in only the highest quality and ethical ingredients to ensure we are creating products we can stand behind.
Our products use: Naturally delivered ingredients; Organic ingredients where is possible; Australian oils, fruits & Extracts; Aromatherapy oils; sustainable & ethical ingredients; natural preservatives.
Our products don't use: sulphates; parabens; phthalates; Petrochemicals; synthetic colours; synthetic fragrances. All label must be design for an amber bottle.
Label Requirements:
* 300 DPI minimum
* All fonts have been outlined
* 3mm Bleed included in artwork
Colors
Designer to choose colors to be used in the design.
Look and feel
Each slider illustrates characteristics of the customer's brand and the style your logo design should communicate.

```html
<!DOCTYPE html>
<html lang="en">
<head>
<meta charset="utf-8">
<title>Leafmerelle – Label Design</title>
<link href="https://fonts.googleapis.com/css2?family=Cormorant+Garamond:wght@500&family=Encode+Sans:wght@300;400&family=Inter:wght@800&display=swap" rel="stylesheet">
<style>
  :root {
    --lid-band: #d3d3d3;
    --wrap-band: #ededed;
    --label-white: #ffffff;
    --ring-grey: #9a9a9a;
    --ink: #111111;
    --fern-green: #c9dcc4;
    --fern-green-soft: #e3ede0;
    --divider: #8c8c8c;
  }
  * { margin: 0; padding: 0; box-sizing: border-box; }
  html, body { width: 1074px; height: 1200px; overflow: hidden; background: var(--label-white); }
  .canvas { width: 1074px; height: 1200px; display: flex; flex-direction: column; }

  .lid-panel {
    height: 600px; background: var(--lid-band);
    border-bottom: 1px solid var(--divider);
    display: flex; align-items: center; justify-content: center;
  }
  .lid-sticker {
    width: 316px; height: 316px; border-radius: 50%;
    background: var(--label-white); border: 3px solid var(--ring-grey);
    display: flex; flex-direction: column; align-items: center; justify-content: center;
    text-align: center; padding-top: 20px;
  }
  .brand-name {
    font-family: "Cormorant Garamond", serif; font-weight: 500;
    font-size: 31px; letter-spacing: 7px; text-transform: uppercase;
    color: var(--ink); margin-left: 7px;
  }
  .brand-tagline {
    font-family: "Encode Sans", sans-serif; font-weight: 300;
    font-size: 15px; letter-spacing: 3.5px; line-height: 19px;
    color: var(--ink); margin-top: 28px; text-transform: uppercase;
  }

  .wrap-panel {
    height: 600px; background: var(--wrap-band);
    display: flex; align-items: center; justify-content: center;
  }
  .wrap-label {
    position: relative; width: 953px; height: 263px;
    background: var(--label-white); overflow: hidden;
  }
  .fern-art { position: absolute; left: 305px; top: 0; width: 235px; height: 263px; }
  .product-title {
    position: absolute; left: 33px; top: 58px;
    font-family: "Inter", sans-serif; font-weight: 800;
    font-size: 55px; line-height: 49px; letter-spacing: -0.5px;
    color: var(--ink); text-transform: uppercase;
  }
  .product-weight {
    position: absolute; left: 33px; top: 212px;
    font-family: "Encode Sans", sans-serif; font-weight: 400;
    font-size: 31px; line-height: 32px; color: var(--ink);
  }
  .label-info {
    position: absolute; left: 506px; top: 16px; width: 420px;
    font-family: "Encode Sans", sans-serif; font-weight: 300;
    font-size: 11.4px; line-height: 14.7px; color: var(--ink);
  }
  .label-info p + p { margin-top: 14.7px; }
</style>
</head>
<body>
<main class="canvas">
  <section class="lid-panel">
    <div class="lid-sticker">
      <div class="brand-name">Leafmerelle</div>
      <div class="brand-tagline">100% Natural,<br>Australian Made<br>Skincare</div>
    </div>
  </section>

  <section class="wrap-panel">
    <div class="wrap-label">
      <svg class="fern-art" role="img" aria-label="Pale green fern frond illustration" viewBox="0 0 235 263" preserveAspectRatio="none">
        <defs>
          <linearGradient id="fernTone" x1="0" y1="0" x2="0" y2="1">
            <stop offset="0" stop-color="var(--fern-green-soft)"/>
            <stop offset="1" stop-color="var(--fern-green)"/>
          </linearGradient>
        </defs>
        <rect width="235" height="263" fill="url(#fernTone)"/>
      </svg>

      <h1 class="product-title">Pink Clay<br>Calming<br>Mask</h1>
      <div class="product-weight">90g</div>

      <div class="label-info">
        <p>Directions: Gently massage in circular motions onto damp skin, avoiding eye area. Rinse away with warm water or face cloth. Follow with your favourite moisturiser. Use morning and night.</p>
        <p>Ingredients: Purified Water, Lauryl Glucoside (Coconut &amp; Sugar Derived), Glycerin*, Cocamido Propyl Betaine (Coconut Derived), Triticum Aestivum Leaf Extract (Wheatgrass), Camellia Sinensis Leaf Extract (Green Tea), Chlorophyll (Alfalfa Grass), Citrus Sinensis (Orange) Oil, Carum Petroselinum Herb Extract (Parsley Seed), Myroxylon Pereirae (Peru Balsam) Oil, Leptospermum Petersonii (Lemon Tea Tree) Oil, Citrus Aurantium Var Amara (Petitgrain) Oil, Tocopherol (Vitamin E), Citric Acid, Hydroxymethylglycinate (Glycine Derived) - * Organic Ingredients</p>
        <p>Store in a cool dry place<br>Caution For external use only. Avoid contact with eyes. If irritation occurs, discontinue use.</p>
      </div>
    </div>
  </section>
</main>
</body>
</html>
```